Business Card Design for a Lending Business (Hard Money loans)

We need a business card for our Real Estate Lending business. We do hard Money loans for real estate investors. We have an existing logo we like, see attached. I'd like the business card to mostly include the logo colors, but a bright color pop of some sort would be nice to see also. Card should include Logo, Company Name, Company Address, Employee Name, Cell Phone, Main Phone, Email, Website

Industry/Entity Type

Finance / Lending

Contact Information for Business Card

Logo, Company Name, Company Address, Employee Name, Cell Phone, Main Phone, Email, Website

Requirements
Nice to have
• I'd like the business card to mostly include the logo colors, but a bright color pop of some sort would be nice to see also.

```html
<!DOCTYPE html>
<html lang="en">
<head>
<meta charset="utf-8">
<title>Harborline Lending – Business Card</title>
<link rel="stylesheet" href="https://fonts.googleapis.com/css2?family=Montserrat:wght@500;700&display=swap">
<style>
  :root {
    --navy: #25357c;
    --navy-deep: #1f2f78;
    --navy-soft: #6a78ab;
    --cyan: #22a9d8;
    --paper: #f1f1f1;
    --white: #ffffff;
    --backdrop: #d4d4d4;
  }
  * { margin: 0; padding: 0; box-sizing: border-box; }
  html, body {
    width: 1200px; height: 1200px; overflow: hidden;
    background: var(--backdrop);
    font-family: "Montserrat", sans-serif;
  }
  .sheet { position: relative; width: 1200px; height: 1200px; }
  .card {
    position: absolute; left: 150px; width: 900px; height: 514px;
    border-radius: 30px; overflow: hidden;
    box-shadow: 0 10px 24px rgba(0,0,0,0.18);
  }
  .card-front {
    top: 60px;
    background: linear-gradient(100deg, var(--navy-soft) 0%, #4f5d9a 35%, var(--navy) 70%, var(--navy-deep) 100%);
    display: flex; align-items: center; justify-content: center;
  }
  .card-back { top: 626px; background: var(--paper); }
  .brand {
    display: flex; align-items: center; gap: 18px;
    font-weight: 700; letter-spacing: 6px; text-transform: uppercase;
    white-space: nowrap;
  }
  .brand-dot { border-radius: 50%; flex: none; }
  .card-front .brand { color: var(--white); font-size: 50px; }
  .card-front .brand-dot { width: 34px; height: 34px; background: var(--white); }
  .back-shapes { position: absolute; inset: 0; width: 900px; height: 514px; }
  .card-back .brand {
    position: absolute; left: 50px; top: 210px;
    color: var(--navy); font-size: 30px; letter-spacing: 4px;
    flex-direction: column; align-items: flex-start; gap: 6px;
  }
  .card-back .brand-dot { width: 26px; height: 26px; background: var(--navy); }
  .details {
    position: absolute; left: 540px; top: 78px; width: 335px;
    color: var(--white); white-space: nowrap;
  }
  .person-name { font-size: 38px; font-weight: 700; }
  .person-title { font-size: 21px; font-weight: 500; margin-top: 6px; }
  .address { font-size: 21px; font-weight: 500; line-height: 1.4; margin-top: 44px; }
  .contacts { list-style: none; margin-top: 26px; font-size: 18px; font-weight: 500; }
  .contacts li { display: flex; align-items: center; gap: 12px; line-height: 1.6; }
  .contacts svg { width: 18px; height: 18px; flex: none; fill: var(--white); }
</style>
</head>
<body>
<main class="sheet">
  <section class="card card-front" aria-label="Card front">
    <div class="brand"><span class="brand-dot"></span>Harborline Lending</div>
  </section>

  <section class="card card-back" aria-label="Card back">
    <svg class="back-shapes" viewBox="0 0 900 514" aria-hidden="true">
      <path d="M240 0 Q470 170 460 514 L900 514 L900 0 Z" fill="var(--cyan)"/>
      <path d="M330 0 Q520 190 470 514 L900 514 L900 0 Z" fill="var(--navy)"/>
    </svg>

    <div class="brand">
      <span class="brand-dot"></span>
      <span>Harborline</span>
      <span>Lending</span>
    </div>

    <div class="details">
      <h1 class="person-name">Marcus Dale</h1>
      <p class="person-title">Founder &amp; Director</p>
      <p class="address">1820 Harbor Mill Rd.<br>Riverton MD 21030</p>
      <ul class="contacts">
        <li><svg viewBox="0 0 24 24"><path d="M6.6 10.8a15 15 0 0 0 6.6 6.6l2.2-2.2a1 1 0 0 1 1-.25 11.4 11.4 0 0 0 3.6.57 1 1 0 0 1 1 1V20a1 1 0 0 1-1 1A17 17 0 0 1 3 4a1 1 0 0 1 1-1h3.5a1 1 0 0 1 1 1c0 1.250.2 2.450.57 3.6a1 1 0 0 1-.25 1z"/></svg>410-555-0142</li>
        <li><svg viewBox="0 0 24 24"><path d="M6 2h12v5H6zM4 8h16a2 2 0 0 1 2 2v7h-4v5H6v-5H2v-7a2 2 0 0 1 2-2zm4 8v4h8v-4z"/></svg>410-555-0187</li>
        <li><svg viewBox="0 0 24 24"><path d="M2 5h20v14H2zm2 2v.5l8 5 8-5V7l-8 5z"/></svg>info@HarborlineLending.com</li>
        <li><svg viewBox="0 0 24 24"><path d="M12 2a10 10 0 1 0 0 20 10 10 0 0 0 0-20zm-1 2.1V11H4.1A8 8 0 0 1 11 4.1zm2 0A8 8 0 0 1 19.9 11H13zM4.1 13H11v6.9A8 8 0 0 1 4.1 13zm8.9 6.9V13h6.9a8 8 0 0 1-6.9 6.9z"/></svg>www.harborlinelending.com</li>
      </ul>
    </div>
  </section>
</main>
</body>
</html>
```